mVT Announcement

Hi,
We would like to create an 8.5"x11" flyer. In PDF (under 5MB), PNG, JPG, and .ai as well.
"Exciting News!

We're upgrading to the advanced mVistaTrack system, enhancing care, streamlining processes, and securing your health information. A brief adjustment period may occur during the upgrade. Insurance card(s) will need to be rescanned, we appreciate your patience. Thank you for being part of our journey towards high-quality healthcare.

Your current patient portal will not be changed at this time.

In health,
Holloway Foot & Ankle "

Attached is our logo, mVT logo and the specific colors of our logo if needed.

Thank you,

```html
<!DOCTYPE html>
<html lang="en">
<head>
<meta charset="utf-8">
<title>Holloway Foot &amp; Ankle – mVistaTrack Announcement</title>
<link href="https://fonts.googleapis.com/css2?family=Poppins:wght@300;400;500;600;700&display=swap" rel="stylesheet">
<style>
  :root{
    --surround:#9b9b9b;
    --paper:#ffffff;
    --ink:#2a2a2a;
    --body:#55566a;
    --orange:#f27b4d;
    --orange-soft:#f49b72;
    --green:#55c096;
    --pill:#e8e8ea;
    --strip:#e6e6e6;
    --navy:#1f3f5e;
  }
  *{margin:0;padding:0;box-sizing:border-box}
  html,body{width:963px;height:1200px;overflow:hidden}
  body{background:var(--surround);font-family:'Poppins',sans-serif;position:relative}
  .flyer{position:absolute;left:49px;top:41px;width:865px;height:1120px;background:var(--paper);overflow:hidden}
  .backdrop{position:absolute;inset:0}
  .brand{position:absolute;right:52px;top:44px;display:flex;align-items:center;gap:12px}
  .brand-mark{width:58px;height:58px;background:var(--green)}
  .brand-name{color:var(--orange);font-weight:700;font-size:26px;line-height:28px;text-align:right;letter-spacing:.5px}
  .brand-name small{display:block;font-size:12px;line-height:16px;letter-spacing:.3px}
  .headline{position:absolute;left:53px;top:86px;font-weight:700;font-size:108px;line-height:1;color:var(--ink);letter-spacing:-1px}
  .headline .accent{position:absolute;left:178px;top:101px;color:var(--orange);white-space:nowrap}
  .headline-rule{position:absolute;left:51px;top:281px;width:157px;height:3px;background:var(--green)}
  .message{position:absolute;left:53px;top:355px;width:785px;font-size:17.6px;line-height:38px;color:var(--body);font-weight:400}
  .message strong{font-weight:600;color:#4a4b5c}
  .partner{float:right;width:215px;height:76px;margin-right:8px;padding-top:2px;text-align:center;color:var(--navy);font-size:26px;font-weight:400;letter-spacing:-.5px;line-height:38px}
  .notice{position:absolute;left:52px;top:580px;width:654px;height:46px;border-radius:8px;background:var(--pill);color:var(--body);font-size:20px;line-height:46px;padding-left:15px}
  .signoff{position:absolute;left:53px;top:655px;font-size:19px;color:var(--body)}
  .signature{position:absolute;left:53px;top:692px;display:flex;align-items:center;gap:10px;font-weight:600;font-size:20.5px;color:#4a4b5c}
  .signature-mark{width:18px;height:18px;border-radius:50%;background:var(--green)}
  .contact{position:absolute;left:52px;color:#fff;font-size:21px;line-height:30px;display:flex;align-items:flex-start;gap:15px}
  .contact svg{flex:none}
  .contact.phone{top:891px}
  .contact.address{top:947px}
  .contact.phone span{line-height:32px}
  .contact.address span{padding-top:1px}
  .photo{position:absolute;left:396px;top:775px;width:417px;height:240px;background:linear-gradient(120deg,#1f3f8a 0%,#2b4f9a 14%,#e9d9cf 30%,#f2c9b0 50%,#f6f1ec 72%,#e8dfd6 100%)}
  .footer{position:absolute;left:0;bottom:0;width:865px;height:51px;background:var(--ink);display:flex;align-items:center;justify-content:center;gap:26px;color:#fff;font-size:20px}
  .footer .rule{width:103px;height:1px;background:#5a5a5a}
</style>
</head>
<body>
<main class="flyer">
  <svg class="backdrop" width="865" height="1120" viewBox="0 0 865 1120" aria-hidden="true">
    <defs>
      <linearGradient id="orangeWash" x1="0" y1="0" x2="1" y2="1">
        <stop offset="0" stop-color="#f07a48"/>
        <stop offset="1" stop-color="#f49a6d"/>
      </linearGradient>
    </defs>
    <rect class="edge-strip" x="841" y="0" width="24" height="700" fill="var(--strip)"/>
    <path class="corner-ring" d="M153,0 A153,153 0 0 1 0,153 L0,112 A112,112 0 0 0 112,0 Z" fill="var(--green)"/>
    <path class="corner-sweep" d="M623,780 Q720,700 865,689 L865,789 Q830,789 813,792 L813,780 Z" fill="var(--green)"/>
    <path class="lower-field" d="M0,723 Q170,842 400,848 L590,848 L590,1064 L0,1064 Z" fill="url(#orangeWash)"/>
    <path class="lower-tab" d="M487,1064 Q487,1030 500,1015 L589,1015 Q593,1040 589,1064 Z" fill="var(--green)"/>
  </svg>

  <div class="brand">
    <div class="brand-mark"></div>
    <div class="brand-name">HOLLOWAY<br>FOOT &amp; ANKLE<small>HOLLOWAYFEET.COM</small></div>
  </div>

  <h1 class="headline">Exciting<span class="accent">News!</span></h1>
  <div class="headline-rule"></div>

  <p class="message">
    <span class="partner">mVistaTrack</span>
    <strong>We're upgrading to the advanced mVistaTrack system,</strong> enhancing care, streamlining processes, and securing your health information. A brief adjustment period may occur during the upgrade. Insurance card(s) will need to be rescanned, we appreciate your patience. Thank you for being part of our journey towards high-quality healthcare.
  </p>

  <div class="notice">Your current patient portal will not be changed at this time.</div>

  <p class="signoff">In health,</p>
  <div class="signature"><span class="signature-mark"></span>Holloway Foot &amp; Ankle</div>

  <div class="contact phone">
    <svg width="32" height="32" viewBox="0 0 32 32" aria-hidden="true">
      <circle cx="16" cy="16" r="15" fill="var(--green)" stroke="#fff" stroke-width="2"/>
      <path d="M11.5,9.5 l3,0 1.2,3.6 -1.8,1.4 q1.3,2.8 3.6,3.6 l1.4,-1.8 3.6,1.2 0,3 q-0.4,1.4 -2,1.4 q-5.6,-0.4 -9.4,-4.6 q-1.8,-2.6 -1.6,-5.8 q0.4,-1.8 2,-2z" fill="#fff"/>
    </svg>
    <span>(555)014-0273</span>
  </div>
  <div class="contact address">
    <svg width="32" height="32" viewBox="0 0 32 32" aria-hidden="true">
      <circle cx="16" cy="16" r="15" fill="var(--green)" stroke="#fff" stroke-width="2"/>
      <path d="M16,7.5 a6,6 0 0 1 6,6 c0,4.5 -6,11 -6,11 s-6,-6.5 -6,-11 a6,6 0 0 1 6,-6z" fill="#fff"/>
      <circle cx="16" cy="13.5" r="2.3" fill="var(--green)"/>
    </svg>
    <span>88 Larkspur Ave.<br>Ste 210, Holloway, MD 20999</span>
  </div>

  <div class="photo" role="img" aria-label="Photo of a podiatrist in gloves examining a patient's bare feet"></div>

  <footer class="footer">
    <span class="rule"></span>
    <span>www.hollowayfeet.com</span>
    <span class="rule"></span>
  </footer>
</main>
</body>
</html>
```